Storm postcards

We need postcards for our roofing company. A recent storm hit our area and we are looking to market to those that were hit in the area. We want something that is simple, but flashy enough to get peoples attention. We are looking for something that has a good blend of flash and professional look.

Name of the company is Brightwell Building Partners LLC

Target Market(s)

Homeowners

Font styles to use
Serif

Requirements
Must have
• Phone number 480-913-2274, The storm was mostly a wind storm, some of the postcards attached are for hail but this one should focus of STORM DAMAGE.
• My business license number has to be on the postcard somewhere preferably small and hidden ROC #284063

```html
<!DOCTYPE html>
<html lang="en">
<head>
<meta charset="utf-8">
<title>Brightwell Building Partners – Storm Postcard</title>
<link rel="stylesheet" href="https://fonts.googleapis.com/css2?family=Roboto:wght@400;500;700&display=swap">
<style>
  :root {
    --brand-blue: #1e8ac6;
    --brand-red: #e0202a;
    --ribbon-dark: #a8121a;
    --ink: #2b2b2b;
    --muted: #8a8a8a;
    --paper: #ffffff;
    --storm-top: #3a2f5c;
    --storm-mid: #8c7fa6;
    --roof-brown: #5a4a3e;
    --house-dark: #2e2620;
  }
  * { margin: 0; padding: 0; box-sizing: border-box; }
  html, body { width: 1200px; height: 848px; overflow: hidden; background: var(--paper); }
  .postcard {
    position: relative;
    width: 1200px;
    height: 848px;
    background: var(--paper);
    font-family: "Roboto", Arial, sans-serif;
    overflow: hidden;
  }
  .postcard__art { position: absolute; inset: 0; }
  .brand {
    position: absolute;
    left: 62px;
    top: 58px;
    display: flex;
    align-items: center;
    gap: 14px;
  }
  .brand__mark { width: 40px; height: 40px; background: var(--brand-blue); }
  .brand__name {
    color: var(--brand-blue);
    font-weight: 700;
    font-size: 30px;
    letter-spacing: 0.5px;
    line-height: 1;
  }
  .headline {
    position: absolute;
    left: 62px;
    top: 158px;
    color: var(--brand-blue);
    font-weight: 500;
    font-size: 36px;
    line-height: 1;
  }
  .facts { position: absolute; left: 46px; top: 218px; list-style: none; }
  .facts__item {
    position: relative;
    padding-left: 21px;
    color: var(--ink);
    font-size: 27px;
    line-height: 33px;
    margin-bottom: 20px;
  }
  .facts__tick { position: absolute; left: 0; top: 9px; width: 18px; height: 16px; }
  .ribbon {
    position: absolute;
    left: 0;
    top: 411px;
    width: 560px;
    height: 165px;
    background: linear-gradient(90deg, #d81c26, var(--brand-red) 60%, #e8303a);
    display: flex;
    align-items: center;
    padding-left: 43px;
  }
  .ribbon__text {
    color: var(--paper);
    font-weight: 700;
    font-size: 80px;
    letter-spacing: -1px;
    line-height: 1;
  }
  .contact { position: absolute; left: 48px; top: 625px; }
  .contact__label {
    color: var(--brand-red);
    font-weight: 700;
    font-size: 35px;
    line-height: 40px;
    padding-left: 3px;
  }
  .contact__phone {
    display: flex;
    align-items: center;
    gap: 10px;
    margin-top: 12px;
    color: var(--brand-red);
    font-weight: 700;
    font-size: 60px;
    line-height: 62px;
  }
  .contact__phone-icon { width: 43px; height: 43px; }
  .contact__email {
    margin-top: 6px;
    padding-left: 5px;
    color: var(--ink);
    font-size: 40px;
    line-height: 50px;
  }
  .license {
    position: absolute;
    left: 53px;
    bottom: 12px;
    color: var(--muted);
    font-size: 13px;
    letter-spacing: 0.5px;
    line-height: 1;
  }
</style>
</head>
<body>
<div class="postcard">
  <svg class="postcard__art" width="1200" height="848" viewBox="0 0 1200 848">
    <defs>
      <clipPath id="photo-clip"><circle cx="989" cy="428" r="505"/></clipPath>
      <linearGradient id="storm-sky" x1="0" y1="0" x2="0" y2="1">
        <stop offset="0" stop-color="var(--storm-top)"/>
        <stop offset="0.35" stop-color="var(--storm-mid)"/>
        <stop offset="0.55" stop-color="var(--roof-brown)"/>
        <stop offset="1" stop-color="var(--house-dark)"/>
      </linearGradient>
    </defs>
    <circle cx="989" cy="428" r="528" fill="none" stroke="var(--brand-red)" stroke-width="13"/>
    <circle cx="989" cy="428" r="512" fill="none" stroke="var(--brand-blue)" stroke-width="8"/>
    <g clip-path="url(#photo-clip)">
      <rect x="440" y="0" width="760" height="848" fill="url(#storm-sky)" role="img" aria-label="Photo of a large house with shingled roof and garage under a purple lightning storm sky"/>
    </g>
    <polygon points="560,411 520,411 560,365" fill="var(--ribbon-dark)"/>
    <polygon points="560,576 520,576 560,622" fill="var(--ribbon-dark)"/>
  </svg>

  <div class="brand">
    <span class="brand__mark"></span>
    <span class="brand__name">Brightwell Building Partners</span>
  </div>

  <h1 class="headline">Local Residents are Getting</h1>

  <ul class="facts">
    <li class="facts__item">
      <svg class="facts__tick" viewBox="0 0 18 16"><path d="M2 9 L7 14 L16 2" fill="none" stroke="var(--brand-red)" stroke-width="3"/></svg>
      Did you know: Strom Damage is<br>Covered by your<br>Homeowners Insurance?
    </li>
    <li class="facts__item">
      <svg class="facts__tick" viewBox="0 0 18 16"><path d="M2 9 L7 14 L16 2" fill="none" stroke="var(--brand-red)" stroke-width="3"/></svg>
      Do You Qualify for a FREE Roof?<br>Should You File A Claim?
    </li>
  </ul>

  <div class="ribbon"><span class="ribbon__text">FREE ROOFS!</span></div>

  <div class="contact">
    <p class="contact__label">CALL US</p>
    <p class="contact__phone">
      <svg class="contact__phone-icon" viewBox="0 0 43 43">
        <rect width="43" height="43" rx="7" fill="var(--ink)"/>
        <path d="M15 9 C11 11 10 16 13 23 C16 30 21 34 26 34 L29 29 L24 25 L21 27 C19 25 17 21 17 18 L20 16 L18 10 Z" fill="var(--paper)"/>
      </svg>
      480-913-2274
    </p>
    <p class="contact__email">sam@brightwellbp.com</p>
  </div>

  <p class="license">ROC #284063</p>
</div>
</body>
</html>
```